Letterhead and Business Card for our company

We need a letterhead to our company with Business Cards.. This will be printed. The letter head is the official use for the company.

Note: Put in consideration that 2 languages will be used, you will design the English and we will add the Arabic.

Company name: Tidewell Partners
City: Jeddah
District: Alrehab
Center: Marlow Square
Country: Saudi Arabia
POBox: 7382 Jeddah 29813

Industry/Entity Type

Startup

Font styles to use
Sans Serif

Requirements
Must have
• Capital: 100,000
• CR: 5817209364

```html
<!DOCTYPE html>
<html lang="en">
<head>
<meta charset="utf-8">
<title>Tidewell Partners – Stationery</title>
<link rel="stylesheet" href="https://fonts.googleapis.com/css2?family=Roboto:wght@400;500;700&display=swap">
<style>
  :root{
    --page:#ffffff;
    --paper:#f9f9f9;
    --card:#34363b;
    --ink:#2b2b2b;
    --ink-soft:#555a60;
    --on-dark:#ffffff;
    --blue:#3a9bd0;
    --green:#6aa51c;
    --red:#d5172b;
    --magenta:#a11a5b;
    --purple:#5b4a9e;
  }
  *{box-sizing:border-box;margin:0;padding:0}
  html,body{width:1200px;height:1200px;overflow:hidden;background:var(--page);font-family:"Roboto",sans-serif}
  .canvas{position:relative;width:1200px;height:1200px}

  /* Letterhead */
  .letterhead{position:absolute;left:448px;top:182px;width:590px;height:836px;background:var(--paper)}
  .letterhead .brand{position:absolute;left:38px;top:60px;display:flex;align-items:center;gap:8px}
  .brand-dot{width:12px;height:12px;border-radius:50%;background:var(--blue)}
  .brand-name{font-weight:500;color:var(--ink-soft);font-size:19px;letter-spacing:.5px}
  .letterhead .address{position:absolute;left:405px;top:53px;font-size:9px;line-height:12.3px;color:var(--ink)}

  /* Business cards */
  .card{position:absolute;left:160px;width:256px;height:155px;background:var(--card);overflow:hidden}
  .card-front{top:435px}
  .card-back{top:609px}
  .card-front .brand{position:absolute;left:0;right:0;top:66px;display:flex;justify-content:center;align-items:center;gap:7px}
  .card .brand-name{color:var(--on-dark);font-size:15px}
  .stripe{position:absolute;left:0;bottom:0;width:100%;height:5px;display:flex}
  .stripe span{flex:1}
  .card-back .mark{position:absolute;left:36px;top:42px;width:26px;height:26px;border-radius:50%;background:var(--blue)}
  .card-back .details{position:absolute;left:132px;top:31px;color:var(--on-dark)}
  .details .name{font-weight:700;font-size:10.5px}
  .details .role{font-size:5.5px;opacity:.85;margin-top:1px}
  .details ul{list-style:none;margin-top:13px;font-size:6.3px;line-height:9.2px}
  .details li{display:flex;align-items:center;gap:5px}
  .details li svg{width:6px;height:6px;fill:var(--on-dark)}
  .details .addr{margin-top:3px;font-size:6.3px;line-height:9.2px}
  .band{position:absolute;left:0;bottom:0;width:100%;height:20px}
  .band .web{position:absolute;left:132px;top:4px;font-size:6.5px;color:var(--on-dark)}
</style>
</head>
<body>
<div class="canvas">

  <section class="letterhead">
    <div class="brand"><span class="brand-dot"></span><span class="brand-name">Tidewell Partners</span></div>
    <div class="address">
      7382 Jeddah 29813<br>
      Marlow Square Jeddah Saudi Arabia<br>
      Capital: 100,000<br>
      CR: 5817209364
    </div>
  </section>

  <section class="card card-front">
    <div class="brand"><span class="brand-dot"></span><span class="brand-name">Tidewell Partners</span></div>
    <div class="stripe">
      <span style="background:var(--blue)"></span>
      <span style="background:var(--green)"></span>
      <span style="background:var(--red)"></span>
      <span style="background:var(--magenta)"></span>
      <span style="background:var(--purple)"></span>
    </div>
  </section>

  <section class="card card-back">
    <span class="mark"></span>
    <div class="details">
      <p class="name">Tidewell Partners</p>
      <p class="role">Managing Director</p>
      <ul>
        <li><svg viewBox="0 0 10 10"><rect x="2.5" y="0" width="5" height="10" rx="1"/></svg>+111 222 3333</li>
        <li><svg viewBox="0 0 10 10"><path d="M0 3 Q5 0 10 3 L8 5 L6.5 3.5 L3.5 3.5 L2 5 Z M2 6 H8 V10 H2 Z"/></svg>+444 555 6666</li>
        <li><svg viewBox="0 0 10 10"><path d="M0 2 H10 V8 H0 Z" /></svg>name@tidewellpartners.com</li>
      </ul>
      <p class="addr">7382 Jeddah 29813<br>Marlow Square Jeddah Saudi Arabia</p>
    </div>
    <svg class="band" viewBox="0 0 256 20" preserveAspectRatio="none">
      <rect x="0" y="10" width="31" height="10" fill="var(--magenta)"/>
      <rect x="31" y="10" width="30" height="10" fill="var(--red)"/>
      <rect x="61" y="10" width="30" height="10" fill="var(--green)"/>
      <rect x="91" y="10" width="30" height="10" fill="var(--purple)"/>
      <polygon points="104,20 122,0 256,0 256,20" fill="var(--blue)"/>
    </svg>
    <div class="band"><span class="web">www.tidewellpartners.com</span></div>
  </section>

</div>
</body>
</html>
```